Real Estate Investment Company needs postcard design

We need a postcard design for a Real Estate Investment company named 'Bright Harbor Holdings, LLC'. We are a residential redevelopment company who specializes in buying distressed homes at a significant discount, and renovate and resell them to retail home buyers and landlords. Our service is to give home owners an option to contact us if they want to sell their home. We would like to see designs that use our logo with a modern and friendly feel. These post cards will be going out to clients who are in stressful situations (foreclosure, estate sales, etc.) and would like them to feel comfortable and safe when receiving this postcard. The final design should communicate stress free and fast solution for their situation.
Real Estate

```html
<!DOCTYPE html>
<html lang="en">
<head>
<meta charset="utf-8">
<title>Bright Harbor Holdings – Seller Postcard</title>
<link href="https://fonts.googleapis.com/css2?family=Oswald:wght@400;500;600&display=swap" rel="stylesheet">
<style>
  :root {
    --page: #ffffff;
    --front-blue: #2b80d2;
    --front-blue-light: #8fc3ef;
    --accent-yellow: #ffd21f;
    --white: #ffffff;
    --back-bg: #e9eef0;
    --back-blue: #1a63b8;
    --ink: #1e1e1e;
    --alert-red: #9d1010;
    --rule: #7d8488;
    --photo-sky: #9fc6e8;
    --photo-house: #d9cbb0;
    --photo-lawn: #4f8f2e;
  }
  * { margin: 0; padding: 0; box-sizing: border-box; }
  html, body {
    width: 805px; height: 1200px; overflow: hidden;
    background: var(--page);
    font-family: "Oswald", "Arial Narrow", sans-serif;
  }
  .postcard {
    position: absolute; left: 42px; width: 720px; height: 555px;
    overflow: hidden;
  }
  .postcard--front { top: 30px; background: var(--front-blue); }
  .postcard--back { top: 610px; background: var(--back-bg); }

  .front-art { position: absolute; inset: 0; }

  .front-copy { position: absolute; left: 25px; top: 0; width: 250px; color: var(--white); }
  .tagline-mark {
    position: absolute; top: 66px; left: 0;
    font-size: 24px; font-weight: 600; color: var(--accent-yellow);
    white-space: nowrap;
  }
  .headline {
    position: absolute; top: 132px; left: 0;
    font-size: 21px; font-weight: 500; line-height: 28px; text-transform: uppercase; white-space: nowrap;
  }
  .headline .hl { color: var(--accent-yellow); }
  .conditions {
    position: absolute; top: 204px; left: 0;
    font-size: 20px; font-weight: 400; line-height: 28px;
  }
  .cta-front {
    position: absolute; top: 296px; left: 2px;
    font-size: 28px; font-weight: 500; color: var(--accent-yellow); white-space: nowrap;
  }
  .brand-name {
    font-weight: 500; text-transform: uppercase; letter-spacing: 0.5px; line-height: 1.1;
    display: flex; align-items: center; gap: 8px;
  }
  .brand-name .brand-dot { width: 12px; height: 12px; background: currentColor; flex: none; }
  .front-copy .brand-name { position: absolute; top: 388px; left: 0; font-size: 24px; color: var(--white); width: 240px; }
  .phone-front {
    position: absolute; top: 462px; left: 0;
    font-size: 34px; font-weight: 600; color: var(--white);
  }

  .back-intro { position: absolute; left: 29px; top: 30px; width: 330px; }
  .back-intro .question { font-size: 18px; font-weight: 500; color: var(--back-blue); text-transform: uppercase; }
  .back-intro .situations { font-size: 16px; line-height: 23px; color: var(--ink); margin-top: 2px; }
  .mascot-slot {
    position: absolute; left: 34px; top: 135px; width: 170px; height: 180px;
    background: radial-gradient(ellipse at center, #6f8fc4 0%, #c9d6e6 70%, var(--back-bg) 100%);
    border-radius: 8px;
  }
  .offer {
    position: absolute; left: 223px; top: 172px;
    font-size: 24px; font-weight: 500; line-height: 29px; color: var(--back-blue); text-transform: uppercase;
  }
  .offer .urgent { color: var(--alert-red); }
  .back-brand { position: absolute; left: 50px; top: 362px; width: 260px; }
  .back-brand .brand-name { font-size: 26px; color: var(--back-blue); }
  .cta-back {
    position: absolute; left: 115px; top: 433px;
    font-size: 24px; font-weight: 500; color: var(--back-blue);
  }
  .phone-back {
    position: absolute; left: 105px; top: 470px;
    font-size: 32px; font-weight: 600; color: var(--back-blue);
  }
  .back-lines { position: absolute; inset: 0; }
</style>
</head>
<body>

<section class="postcard postcard--front">
  <svg class="front-art" width="720" height="555" viewBox="0 0 720 555">
    <defs>
      <linearGradient id="photoTone" x1="0" y1="0" x2="0" y2="1">
        <stop offset="0" stop-color="var(--photo-sky)"/>
        <stop offset="0.45" stop-color="var(--photo-house)"/>
        <stop offset="1" stop-color="var(--photo-lawn)"/>
      </linearGradient>
    </defs>
    <path d="M346 0 C300 80 262 170 258 270 C255 380 272 470 300 555 L324 555 C296 470 279 380 282 270 C286 170 322 80 372 0 Z" fill="var(--front-blue-light)"/>
    <path role="img" aria-label="Photo of a happy family with a baby cheering in front of their home, holding a SOLD sign beside a For Sale sign"
      d="M372 0 C322 80 286 170 282 270 C279 380 296 470 324 555 L720 555 L720 0 Z" fill="url(#photoTone)"/>
  </svg>

  <div class="front-copy">
    <div class="tagline-mark">Sell Easy Today</div>
    <div class="headline">We will pay <span class="hl">cash</span> for<br>your house - <span class="hl">as is!</span></div>
    <div class="conditions">Any condition<br>Any situation</div>
    <div class="cta-front">CALL US TODAY!</div>
    <div class="brand-name"><span class="brand-dot"></span>Bright Harbor Holdings, LLC</div>
    <div class="phone-front">555-310-2468</div>
  </div>
</section>

<section class="postcard postcard--back">
  <svg class="back-lines" width="720" height="555" viewBox="0 0 720 555">
    <path d="M364 40 C380 150 360 260 356 340 C352 420 362 480 368 505" fill="none" stroke="var(--back-blue)" stroke-width="3" stroke-linecap="round"/>
    <rect x="591" y="39" width="100" height="107" fill="none" stroke="var(--rule)" stroke-width="1.5" stroke-dasharray="6 4"/>
    <g stroke="var(--rule)" stroke-width="1.5" stroke-dasharray="7 5">
      <line x1="369" y1="312" x2="690" y2="312"/>
      <line x1="369" y1="362" x2="690" y2="362"/>
      <line x1="369" y1="411" x2="690" y2="411"/>
    </g>
  </svg>

  <div class="back-intro">
    <div class="question">Thinking about selling?</div>
    <div class="situations">Too many repairs? Relocating? Behind on payments? Problem tenants? Probate? Foreclosure?</div>
  </div>

  <div class="mascot-slot" role="img" aria-label="Cartoon football player mascot holding a small house and a stack of cash"></div>

  <div class="offer">Get a cash<br>offer on<br>your house<br><span class="urgent">fast!</span></div>

  <div class="back-brand">
    <div class="brand-name"><span class="brand-dot"></span>Bright Harbor Holdings, LLC</div>
  </div>

  <div class="cta-back">CALL US TODAY!</div>
  <div class="phone-back">555-310-2468</div>
</section>

</body>
</html>
```